A Flyer for a clinic/hospital waiting room to warn about patients that they must not abuse our staff

we need a flyer (text attached) with a background of a female nurse or medical doctor photo. I like the example photo where there are four headless satff lined up - something like this, indicating that we are a team and will not tolerate abuse
A4
the text will be over the photo.

Target Market(s)

patients who come to our clinic

Industry/Entity Type

medicine - urology

Colors
0054AA
0677BA
7BADD7
CADEEF
E8F1F8
0094D4
00A9DD
6FCCEA
C7EBF8
E9F6FB

Requirements
Must have
• a photo taking up the whole A4, and text over this. The photos I haev sent are just examples - I will need yo to source a photo
Nice to have
• Horizontal A4 and vertical A4 options. Please add our logo in small , in the bottom right corner

```html
<!DOCTYPE html>
<html lang="en">
<head>
<meta charset="utf-8">
<title>Zero-tolerance flyer – Riverside Urology Clinic</title>
<link rel="stylesheet" href="https://fonts.googleapis.com/css2?family=Inter+Tight:wght@400;600;700;800&display=swap">
<style>
  :root {
    --stage: #9cc4da;
    --paper: #ffffff;
    --band-blue: #5aa0da;
    --accent-blue: #5a9fdc;
    --ink: #222222;
    --text-white: #ffffff;
    --veil: rgba(150, 158, 166, 0.55);
    --photo-light: #dfe8ee;
    --photo-mid: #a9cde6;
    --photo-deep: #3f8fc9;
    --brand: #2f3e4d;
  }
  * { box-sizing: border-box; margin: 0; padding: 0; }
  html, body {
    width: 1009px; height: 1200px; overflow: hidden;
    background: var(--stage);
  }
  body { font-family: "Inter Tight", Arial, sans-serif; }

  .flyer {
    position: absolute; left: 94px; top: 20px;
    width: 820px; height: 1160px;
    background: var(--paper);
    overflow: hidden;
  }

  .hero-photo {
    position: absolute; left: 0; top: 0; width: 820px; height: 520px;
    background:
      radial-gradient(ellipse 55% 80% at 72% 55%, var(--photo-deep) 0%, #5aa6d8 45%, transparent 75%),
      linear-gradient(100deg, var(--photo-light) 0%, #c5d6df 35%, var(--photo-mid) 60%, #7fb7dd 100%);
  }

  .headline-veil {
    position: absolute; left: 26px; top: 24px; width: 485px; height: 473px;
    background: var(--veil);
  }

  .headline { position: absolute; color: var(--text-white); letter-spacing: -0.045em; font-weight: 700; white-space: nowrap; }
  .headline--lead { left: 66px; top: 50px; font-size: 47px; line-height: 1; }
  .headline--tolerance {
    left: 62px; top: 101px; width: 407px; height: 82px;
    background: var(--accent-blue);
    font-size: 63px; line-height: 80px; padding-left: 13px;
  }
  .headline--of { left: 66px; top: 188px; font-size: 47px; line-height: 1; }
  .headline--aggressive {
    left: 65px; top: 240px; width: 406px; height: 168px;
    background: var(--ink);
    font-size: 84px; line-height: 75px; padding: 8px 0 0 12px;
    letter-spacing: -0.04em;
  }
  .headline--respect {
    left: 66px; top: 414px; font-size: 28.5px; line-height: 32px;
    letter-spacing: -0.05em;
  }

  .definition-band {
    position: absolute; left: 0; top: 520px; width: 820px; height: 284px;
    background: var(--band-blue);
    color: var(--text-white);
  }
  .definition-band h2 {
    position: absolute; left: 28px; top: 22px;
    font-size: 28px; font-weight: 700; letter-spacing: -0.05em; white-space: nowrap;
  }
  .behaviour-list { list-style: none; }
  .behaviour-list li {
    position: absolute; font-size: 23.5px; line-height: 25px; font-weight: 400;
    letter-spacing: -0.04em;
  }
  .behaviour-list li::before {
    content: ""; position: absolute; left: -51px; top: 11px;
    width: 33px; height: 4px; background: var(--ink);
  }
  .col-left { left: 79px; }
  .col-right { left: 483px; }
  .row-1 { top: 70px; }
  .row-2 { top: 113px; }
  .row-3 { top: 178px; }

  .support-bar {
    position: absolute; left: 265px; top: 768px; width: 555px; height: 67px;
    background: var(--ink); color: var(--text-white);
    font-size: 23.5px; font-weight: 700; line-height: 29px; letter-spacing: -0.05em;
    padding: 5px 0 0 21px;
  }

  .policy-text {
    position: absolute; left: 28px; color: var(--ink);
    font-size: 21px; line-height: 31px; letter-spacing: -0.045em;
  }
  .policy-text--removal { top: 847px; width: 770px; }
  .policy-text--charges { top: 924px; width: 770px; }
  .policy-text--stance { top: 1008px; width: 540px; }

  .brand-mark {
    position: absolute; left: 590px; top: 1040px; width: 190px;
    display: flex; flex-direction: column; align-items: center; gap: 8px;
  }
  .brand-mark__dot {
    width: 46px; height: 46px; border-radius: 50%;
    background: var(--accent-blue);
  }
  .brand-mark__name {
    font-size: 20px; font-weight: 600; color: var(--brand);
    letter-spacing: -0.02em; white-space: nowrap;
  }
</style>
</head>
<body>
  <main class="flyer">
    <div class="hero-photo" role="img" aria-label="Photo of a nurse in blue scrubs standing with folded arms, with blurred clinic colleagues behind"></div>

    <div class="headline-veil"></div>
    <p class="headline headline--lead">We have</p>
    <p class="headline headline--tolerance">zero-tolerance</p>
    <p class="headline headline--of">for any form of</p>
    <h1 class="headline headline--aggressive">Aggressive<br>behaviour!</h1>
    <p class="headline headline--respect">Our staff treat you with respect &amp;<br>we expect the same in return</p>

    <section class="definition-band">
      <h2>Aggressive behaviour (in-person or on the telephone) is:</h2>
      <ul class="behaviour-list">
        <li class="col-left row-1">Verbal harassment / Swearing</li>
        <li class="col-left row-2">Any verbal or physical<br>confrontation</li>
        <li class="col-left row-3">Raising your voice or<br>making unreasonable<br>demands</li>
        <li class="col-right row-1">Making threats to our staff</li>
        <li class="col-right row-2">Abusive or intimidating<br>behaviour</li>
        <li class="col-right row-3">Sexual or suggestive<br>language or behaviour</li>
      </ul>
    </section>

    <p class="support-bar">If any of our staff feel intimidated in any way,<br>we will always support them.</p>

    <p class="policy-text policy-text--removal">Incidents will result in your immediate removal from the facility, termination of your relationship with the practice, and may result in prosecution.</p>
    <p class="policy-text policy-text--charges">In all circumstances we will support any staff member who wishes to press charges against a perpetrator of aggressive behaviour.</p>
    <p class="policy-text policy-text--stance">We take this stance because our staff work extremely hard in busy circumstances to help you and we will no longer tolerate any form of aggression or abuse.</p>

    <div class="brand-mark">
      <span class="brand-mark__dot"></span>
      <span class="brand-mark__name">Riverside Urology Clinic</span>
    </div>
  </main>
</body>
</html>
```